Bref créative
Business Card and Stationery for Voice and Data Company
Looking for a high tech and modern design
Use same font as used in my logo
See supplied artwork
Professional
Owen Castellan
Owner
P.O. Box 4382 Broomfield, CO 80049
Owen@qvlinkgrid.com
www.qvlinkgrid.com
On the back of the business card, we would like to see a few different drafts:
1) Include Zentro and Bx&q logos and text listed in the Back of the business card section:
2) Include our logo, url of our website, and the text in the back of the business card section
3) Include picture of digital phone, the text in the back of the business card section, our logo, and url to our website
4) Any combination of the drafts above. Feel free to be creative.
We want the following services as bullet points:
Voice and Data Solutions
Structured Cabling
IP Surveillance Cameras

```html
<!DOCTYPE html>
<html lang="en">
<head>
<meta charset="utf-8">
<title>Quarry Vale LinkGrid – Business Card</title>
<link rel="stylesheet" href="https://fonts.googleapis.com/css2?family=Open+Sans:wght@400;600;700;800&display=swap">
<style>
  :root {
    --stage: #ecebe8;
    --brand-green: #6bb23a;
    --brand-green-dark: #4e9a2a;
    --brand-green-light: #86c24c;
    --ink: #3d3d3d;
    --ink-soft: #777777;
    --band-grey: #8a8a8a;
    --band-grey-light: #d4d4d4;
    --paper: #ffffff;
    --blue: #3b7fc4;
  }
  * { margin: 0; padding: 0; box-sizing: border-box; }
  html, body { width: 1200px; height: 629px; overflow: hidden; }
  body {
    background: var(--stage);
    font-family: "Open Sans", Arial, sans-serif;
    position: relative;
  }
  .card {
    position: absolute;
    top: 166px;
    width: 520px;
    height: 297px;
    border-radius: 4px;
    overflow: hidden;
    box-shadow: 0 6px 18px rgba(0,0,0,0.18);
  }
  /* Back */
  .card-back {
    left: 60px;
    background: radial-gradient(circle at 50% 45%, var(--brand-green-light) 0%, var(--brand-green) 55%, var(--brand-green-dark) 100%);
    display: flex;
    align-items: center;
    justify-content: center;
  }
  .back-mark {
    display: flex;
    align-items: center;
    gap: 10px;
  }
  .back-mark .mark-square {
    width: 22px; height: 22px;
    background: var(--paper);
  }
  .back-mark .mark-name {
    color: var(--paper);
    font-weight: 800;
    font-size: 24px;
    letter-spacing: 1px;
  }
  .back-url {
    position: absolute;
    left: 26px;
    bottom: 60px;
    transform-origin: left bottom;
    transform: rotate(-90deg) translateY(100%);
    color: var(--paper);
    font-size: 13px;
    font-weight: 600;
    letter-spacing: 2px;
  }
  /* Front */
  .card-front {
    left: 620px;
    background: var(--paper);
  }
  .brand {
    position: absolute;
    left: 44px;
    top: 52px;
    display: flex;
    align-items: center;
    gap: 12px;
  }
  .brand .mark-square {
    width: 34px; height: 34px;
    background: var(--brand-green);
  }
  .brand-text { text-align: right; }
  .brand-name {
    color: var(--brand-green);
    font-weight: 800;
    font-size: 25px;
    line-height: 1;
    letter-spacing: 0.5px;
  }
  .brand-sub {
    color: var(--ink-soft);
    font-weight: 600;
    font-size: 14px;
    margin-top: 3px;
  }
  .person {
    position: absolute;
    left: 44px;
    top: 146px;
  }
  .person-name { color: var(--blue); font-weight: 700; font-size: 12px; }
  .person-title { color: var(--ink-soft); font-size: 10px; }
  .contact {
    position: absolute;
    left: 330px;
    top: 40px;
    list-style: none;
  }
  .contact li {
    display: flex;
    align-items: center;
    gap: 7px;
    color: var(--ink);
    font-size: 10px;
    height: 18px;
  }
  .contact svg { width: 12px; height: 12px; flex: none; }
  .address {
    position: absolute;
    left: 44px;
    top: 200px;
    color: var(--ink-soft);
    font-size: 9.5px;
  }
  .footer-rule {
    position: absolute;
    left: 0; right: 0;
    bottom: 26px;
    height: 2px;
    background: var(--band-grey-light);
  }
  .footer-band {
    position: absolute;
    left: 0; right: 0;
    bottom: 0;
    height: 18px;
    background: var(--brand-green);
  }
</style>
</head>
<body>
  <section class="card card-back" aria-label="Business card back">
    <div class="back-mark">
      <span class="mark-square"></span>
      <span class="mark-name">QUARRY VALE</span>
    </div>
    <p class="back-url">www.QVLinkgrid.com</p>
  </section>

  <section class="card card-front" aria-label="Business card front">
    <div class="brand">
      <span class="mark-square"></span>
      <div class="brand-text">
        <p class="brand-name">QUARRY VALE</p>
        <p class="brand-sub">LinkGrid, Inc</p>
      </div>
    </div>

    <div class="person">
      <p class="person-name">Owen Castellan</p>
      <p class="person-title">Owner</p>
    </div>

    <ul class="contact">
      <li><svg viewBox="0 0 12 12"><circle cx="6" cy="6" r="6" fill="#6bb23a"/><path d="M4 3l1.2 1.3-.6.8a4 4 0 0 0 2.3 2.3l.8-.6L9 8l-.8.9C5.8 8.7 3.3 6.2 3.1 3.8z" fill="#fff"/></svg>303.555.0186</li>
      <li><svg viewBox="0 0 12 12"><circle cx="6" cy="6" r="6" fill="#6bb23a"/><rect x="3.3" y="4" width="5.4" height="4.5" fill="#fff"/></svg>303.555.0187</li>
      <li><svg viewBox="0 0 12 12"><circle cx="6" cy="6" r="6" fill="#6bb23a"/><rect x="3" y="4" width="6" height="4" fill="#fff"/><path d="M3 4l3 2.3L9 4" stroke="#6bb23a" stroke-width=".7" fill="none"/></svg>Owen@qvlinkgrid.com</li>
      <li><svg viewBox="0 0 12 12"><circle cx="6" cy="6" r="6" fill="#6bb23a"/><circle cx="6" cy="6" r="3" fill="none" stroke="#fff" stroke-width=".9"/><path d="M3 6h6M6 3v6" stroke="#fff" stroke-width=".7"/></svg>www.qvlinkgrid.com</li>
    </ul>

    <p class="address">P.O. Box 4382 Broomfield, CO 80049</p>

    <div class="footer-rule" aria-hidden="true"></div>
    <div class="footer-band" aria-hidden="true"></div>
  </section>
</body>
</html>
```